Vow Lanterns - Outdoor Ceremony Designs

We set up wedding ceremonies outside in parks in and beaches. The advert will be in magazines. The design needs to look trendy but sophisticated and show a range of our products in different locations. Here is our website if you need any idea's www.vowlanterns.com.au please ask questions.

Target Market(s)

Females ages 25 to 35

Industry/Entity Type

Wedding

Requirements
Must have
• Spec for the magazine that the ad will be going into:
• HALF PAGE (LANDSCAPE):
• 284MM X 95MM (Width x Height) NO BLEED
• SUPPLY
• ARTWORK SPECIFICATIONS
• SUBMITTING YOUR ARTWORK
• If you are providing us with your own artwork, it is your responsibility to make sure it is set up correctly and to all our required specifications. If it is not, you may be charged an additional fee. We have the right to refuse your artwork if it does not reflect the quality standard of our brochure.
• YOU CAN SEND YOUR ARTWORK VIA CD/DVD OR EMAIL
• ARTWORK SPECIFICATIONS
• Please supply a Commercial Print Ready PDF or JPEG document only.
• IMAGES: All images used in your artwork must be a resolution of 300dpi or above 1mb. Below this will not be accepted.
• FONTS: All fonts must be outlined and embedded. No fonts should go below 8pt for visibility purposes.
• COLOURS: CMYK not RGB. Please remove all spot colours; we will not accept artwork with spot colours.
• BLEED: Only required for a full page advertisement, no bleed is required on any of the other advertisement artwork sizes.
• If any changes need to be made to the clients existing artwork there maybe an additional fee charged and will be on a case by case basis. Please note that working art files will be required, for example a packaged idml or eps with fonts supplied.
• ADVERTISEMENT SELECTION
• 3. HALF PAGE (LANDSCAPE):
• BLEED IS ONLY REQUIRED FOR THE FULL PAGE, NO BLEED IS REQUIRED ON THE OTHER ADVERTISEMENT ARTWORK.
Nice to have
• Outdoor Ceremony Designs - Ph: 0472 318 694
• www.vowlanterns.com.au

```html
<!DOCTYPE html>
<html lang="en">
<head>
<meta charset="utf-8">
<title>Vow Lanterns – Outdoor Ceremony Designs</title>
<link rel="stylesheet" href="https://fonts.googleapis.com/css2?family=Open+Sans:wght@400&display=swap">
<style>
  :root {
    --page-bg: #eceeef;
    --linen-light: #c9e9ec;
    --linen-mid: #a9dce1;
    --linen-deep: #93d1d7;
    --ink: #2b2b2b;
    --badge-teal: #22b3bf;
    --white: #ffffff;
  }
  * { box-sizing: border-box; margin: 0; padding: 0; }
  html, body {
    width: 1200px;
    height: 760px;
    overflow: hidden;
    background: var(--page-bg);
  }
  .advert {
    position: absolute;
    left: 0;
    top: 180px;
    width: 1200px;
    height: 400px;
    background: linear-gradient(180deg, var(--linen-light) 0%, var(--linen-mid) 55%, var(--linen-deep) 100%);
    font-family: "Open Sans", sans-serif;
    color: var(--ink);
    overflow: hidden;
  }
  .brand-name {
    position: absolute;
    left: 40px;
    top: 66px;
    font-family: "Open Sans", sans-serif;
    font-weight: 400;
    font-size: 68px;
    line-height: 80px;
    letter-spacing: 1px;
    color: var(--ink);
    display: flex;
    align-items: center;
    gap: 18px;
    white-space: nowrap;
  }
  .brand-dot {
    width: 14px;
    height: 14px;
    border-radius: 50%;
    background: var(--ink);
    flex: none;
  }
  .tagline {
    position: absolute;
    left: 668px;
    top: 64px;
    width: 510px;
    font-size: 18px;
    line-height: 34px;
    color: var(--ink);
  }
  .photo-strip {
    position: absolute;
    left: 0;
    top: 215px;
    width: 1200px;
    height: 127px;
    display: flex;
  }
  .photo { height: 100%; }
  .photo--beach-aisle { width: 211px; background: linear-gradient(180deg, #6fa6d8 0%, #b9d6ee 45%, #e9eef0 70%, #d8cfc0 100%); }
  .photo--lilies { width: 119px; background: linear-gradient(135deg, #2f6d2a 0%, #8fb17a 45%, #f2f3ee 70%, #5f8a45 100%); }
  .photo--forest-lawn { width: 210px; background: linear-gradient(180deg, #1e3d2a 0%, #2d5a36 55%, #97a83a 75%, #b6b845 100%); }
  .photo--flower-vase { width: 120px; background: linear-gradient(180deg, #f4f4f2 0%, #e8ecef 55%, #9fc1df 80%, #3f6e9c 100%); }
  .photo--garden-aisle { width: 207px; background: linear-gradient(180deg, #3f5a2e 0%, #6f8a4a 40%, #7fa553 70%, #5f8b35 100%); }
  .photo--coastal-lawn { width: 333px; background: linear-gradient(180deg, #b9d4ee 0%, #5e9bd2 35%, #3a8f9c 52%, #7aa15a 70%, #eef0ee 100%); }
  .badge {
    position: absolute;
    left: 848px;
    top: 192px;
    width: 170px;
    height: 170px;
    border-radius: 50%;
    background: var(--badge-teal);
    display: flex;
    align-items: center;
    justify-content: center;
    text-align: center;
    color: var(--white);
    font-family: "Open Sans", sans-serif;
    font-weight: 400;
    font-size: 17px;
    line-height: 24px;
  }
  .contact-line {
    position: absolute;
    left: 30px;
    top: 352px;
    font-size: 20px;
    line-height: 28px;
    color: var(--ink);
    white-space: nowrap;
  }
  .contact-sep { margin: 0 12px; }
</style>
</head>
<body>
  <section class="advert" aria-label="Vow Lanterns half page advertisement">
    <h1 class="brand-name"><span class="brand-dot" aria-hidden="true"></span>Vow Lanterns</h1>

    <p class="tagline">Whether you are planning a garden wedding, a relaxed coastal ceremony, or a lavish affair, we can create a ceremony that leaves your guests saying wow</p>

    <div class="photo-strip">
      <div class="photo photo--beach-aisle" role="img" aria-label="Beach ceremony aisle with white chairs and arbour"></div>
      <div class="photo photo--lilies" role="img" aria-label="White lilies and roses among green leaves"></div>
      <div class="photo photo--forest-lawn" role="img" aria-label="Lawn before a tall forest with a love sign"></div>
      <div class="photo photo--flower-vase" role="img" aria-label="White flower balls in glass vases by the sea"></div>
      <div class="photo photo--garden-aisle" role="img" aria-label="Garden ceremony with white aisle runner and pedestals"></div>
      <div class="photo photo--coastal-lawn" role="img" aria-label="Clifftop lawn ceremony with lanterns and ocean view"></div>
    </div>

    <p class="badge">outdoor<br>ceremony<br>designs</p>

    <p class="contact-line">info@vowlanterns.com.au<span class="contact-sep">•</span>0472 318 694<span class="contact-sep">•</span>www.vowlanterns.com.au</p>
  </section>
</body>
</html>
```